Horticulture Business Card Design Project

New garden service venture, I'd like design to reflect business name, Copper Lantern garden services. Needs to be professional non comical and include a pic. I'd like to see designs in browns and greens as it will be printed on recycled paper to promote sustainability. I'd prefer a modern professonal card that is simple and catchy.
Updates

Thank u to all that submitted design/s -I really appreciated all of them.

Target Market(s)

Professional people aged between 40-60, that own their own homes and enjoy their gardens. Wanting a premium service that can be recommended to others by handing out the card and conveying a professional card that is impressive to potential clients.

Industry/Entity Type

Business

Requirements
Must have
• Picture relating to horticulture. One sided and including business name- Copper Lantern Garden Services, Qualified Horticulturist, name, mobile number and email. Website is not needed. Id like a large green leaf pic such as monstera, ficus lyrata or rhaphis palms etc. Im open to ideas and welcome new suggestions. Simple fonts please
Nice to have
• Large green leaf as pic. Possibly like monstera or similar in size and impact. A modern touch
Should not have
• Comical pic

```html
<!DOCTYPE html>
<html lang="en">
<head>
<meta charset="utf-8">
<title>Copper Lantern Garden Services – Business Card</title>
<link rel="stylesheet" href="https://fonts.googleapis.com/css2?family=Kameron:wght@400&display=swap">
<style>
  :root {
    --page-bg: #ebebeb;
    --card-white: #ffffff;
    --header-grey-top: #e4e4e4;
    --header-grey-bottom: #f7f7f7;
    --leaf-green: #7cbd3a;
    --text-white: #ffffff;
  }
  html, body {
    margin: 0;
    padding: 0;
    width: 1200px;
    height: 900px;
    overflow: hidden;
    background: var(--page-bg);
  }
  .business-card {
    position: absolute;
    left: 100px;
    top: 134px;
    width: 1000px;
    height: 632px;
    background: var(--card-white);
    font-family: "Kameron", Georgia, serif;
    overflow: hidden;
  }
  .card-header {
    position: absolute;
    left: 0;
    top: 0;
    width: 100%;
    height: 192px;
    background: linear-gradient(to bottom, var(--header-grey-top), var(--header-grey-bottom));
  }
  .brand-dot {
    position: absolute;
    left: 34px;
    top: 42px;
    width: 104px;
    height: 104px;
    border-radius: 50%;
    background: var(--leaf-green);
  }
  .company-name {
    position: absolute;
    right: 26px;
    top: 70px;
    margin: 0;
    font-size: 35px;
    font-weight: 400;
    line-height: 1;
    text-transform: uppercase;
    letter-spacing: 1px;
    word-spacing: 8px;
    color: var(--leaf-green);
  }
  .header-rule {
    position: absolute;
    left: 0;
    top: 196px;
    width: 100%;
    height: 11px;
    background: var(--leaf-green);
  }
  .person {
    position: absolute;
    left: 36px;
    top: 320px;
  }
  .person-name {
    margin: 0;
    font-size: 86px;
    font-weight: 400;
    line-height: 1;
    word-spacing: 12px;
    color: var(--leaf-green);
  }
  .person-title {
    margin: 6px 0 0 2px;
    font-size: 33px;
    line-height: 1;
    word-spacing: 6px;
    color: var(--leaf-green);
  }
  .contact-band {
    position: absolute;
    left: 0;
    bottom: 0;
    width: 100%;
    height: 96px;
    background: var(--leaf-green);
    display: flex;
    align-items: center;
    padding: 0 26px 0 36px;
    box-sizing: border-box;
    color: var(--text-white);
    font-size: 29px;
    white-space: pre;
  }
</style>
</head>
<body>
  <article class="business-card">
    <header class="card-header">
      <span class="brand-dot" aria-hidden="true"></span>
      <h1 class="company-name">Copper Lantern Garden Services</h1>
    </header>
    <div class="header-rule"></div>
    <section class="person">
      <h2 class="person-name">Dane Worrell</h2>
      <p class="person-title">Qualified Horticulturist</p>
    </section>
    <footer class="contact-band">Mobile  :  +66870005418   |   Email  :   dane@cl-gardenservices.com</footer>
  </article>
</body>
</html>
```